New Zealand Export company needs business cards

We need new business cards to match our new logo for a company based in New Zealand who deal specifically with the Pacific Islands. We source, consolidate and ship products out of New Zealand to the Pacific Islands. Will attach our old ones and also new logo.
Would like the Islands we deal with and the areas of work we have access to, to be included on the business cards.

Contact Information for Business Card

T +64 9 571 3048
F +64 9 571 6285
12-18 Kowhai Lane, Drury, 2113
PO Box 814, Drury, Auckland 2247, New Zealand
www.falconfreight.example.nz
E sales@falconfreight.example.nz

Font styles to use
Sans Serif

Colors
85abd2
33a6d7
ffffff

Requirements
Must have
• A company of PWM

```html
<!DOCTYPE html>
<html lang="en">
<head>
<meta charset="utf-8">
<title>Falcon Freight – Business Card</title>
<link href="https://fonts.googleapis.com/css2?family=Lato:wght@400;700;900&display=swap" rel="stylesheet">
<style>
  :root {
    --navy: #0b57a2;
    --sky: #41bce8;
    --paper: #ffffff;
    --ink: #1f1f1f;
    --backdrop: #e0e0e0;
  }
  * { margin: 0; padding: 0; box-sizing: border-box; }
  html, body {
    width: 1200px; height: 1200px; overflow: hidden;
    background: var(--backdrop);
    font-family: "Lato", sans-serif;
  }
  .card {
    position: absolute; left: 180px; width: 840px; height: 480px; overflow: hidden;
  }
  .card--front { top: 80px; background: var(--paper); }
  .card--back { top: 638px; background: var(--navy); }

  .brand {
    position: absolute; display: flex; align-items: center; gap: 12px;
    font-weight: 900; letter-spacing: 1px; white-space: nowrap;
  }
  .brand__mark { display: block; background: var(--sky); }
  .card--front .brand { left: 40px; top: 208px; height: 64px; font-size: 31px; color: var(--navy); }
  .card--front .brand__mark { width: 22px; height: 22px; }
  .card--back .brand { left: 0; right: 0; top: 200px; height: 84px; justify-content: center; font-size: 48px; color: var(--paper); gap: 18px; }
  .card--back .brand__mark { width: 32px; height: 32px; }

  .contact {
    position: absolute; right: 40px; top: 182px; list-style: none;
    font-size: 19px; color: var(--ink); text-align: right;
  }
  .contact li { display: flex; align-items: center; justify-content: flex-end; gap: 10px; height: 29.5px; }
  .contact svg { width: 18px; height: 18px; flex: none; }
  .tab {
    position: absolute; right: 0; top: 180px; width: 16px; height: 122px;
    background: var(--sky); border-radius: 8px 0 0 8px;
  }
  .address {
    position: absolute; left: 0; right: 0; top: 424px; text-align: center;
    font-size: 19px; color: var(--ink); white-space: nowrap;
  }
  .band { position: absolute; left: 0; bottom: 0; width: 840px; height: 30px; }
  .web {
    position: absolute; left: 0; right: 0; top: 424px; text-align: center;
    font-size: 19px; color: var(--paper);
  }
</style>
</head>
<body>
  <section class="card card--front">
    <div class="brand"><span class="brand__mark"></span>FALCON FREIGHT</div>

    <ul class="contact">
      <li>+64 9 571 3048
        <svg viewBox="0 0 24 24"><path fill="#0b57a2" d="M6.6 2.5l3 3.6-1.8 2.4c1.2 2.9 3.6 5.3 6.5 6.6l2.4-1.8 3.6 3-1.6 3.4C11.4 19.4 4.6 12.6 3.2 4.1z"/></svg>
      </li>
      <li>+64 9 571 6285
        <svg viewBox="0 0 24 24"><rect x="4" y="10" width="16" height="10" rx="2" fill="#0b57a2"/><rect x="7" y="3" width="10" height="8" fill="none" stroke="#0b57a2" stroke-width="2"/><rect x="8" y="14" width="8" height="2" fill="#fff"/></svg>
      </li>
      <li>sales@falconfreight.example.nz
        <svg viewBox="0 0 24 24"><rect x="2" y="5" width="20" height="14" fill="#0b57a2"/><path d="M2 5l10 8 10-8M2 19l8-7M22 19l-8-7" stroke="#fff" stroke-width="1.5" fill="none"/></svg>
      </li>
      <li>www.falconfreight.example.nz
        <svg viewBox="0 0 24 24"><circle cx="12" cy="12" r="9" fill="none" stroke="#0b57a2" stroke-width="2"/><path d="M3 12h18M12 3c-3 3-3 15 0 18M12 3c3 3 3 15 0 18" fill="none" stroke="#0b57a2" stroke-width="1.5"/></svg>
      </li>
    </ul>
    <div class="tab"></div>

    <p class="address">12-18 Kowhai Lane, Drury, 2113 PO Box 814, Drury, Auckland 2247, New Zealand</p>

    <svg class="band" viewBox="0 0 840 30" preserveAspectRatio="none">
      <polygon points="0,0 598,0 580,30 0,30" fill="#41bce8"/>
      <polygon points="610,0 840,0 840,30 592,30" fill="#0b57a2"/>
    </svg>
  </section>

  <section class="card card--back">
    <div class="brand"><span class="brand__mark"></span>FALCON FREIGHT</div>
    <p class="web">www.falconfreight.example.nz</p>
  </section>
</body>
</html>
```